Health Education Non-Profit Needs a Designer to Layout Magazine (Contest)

Hello, we are looking for someone to layout our print magazine. We'd like to work with someone who also has graphic design experience manipulating photos (see 2 sample issue links below for examples). Ad design is also needed. We like the current design of our magazine, so we are hoping our next designer can maintain the same look and feel as our previous magazines. Samples of our past two issues can be found at https://www.harbolwellness.org/wp-content/uploads/2019/03/issue-09-feb-2019.pdf and https://www.harbolwellness.org/wp-content/uploads/2018/11/the-bright-almanac-2018-05-issue-08.pdf

There are typically 2-4 different issues per year with around 11 articles in each issue. Issues are 24 pages. If there is a lot of white space, we may ask the designer to design an ad at the end of the article. We are looking to work with someone who is responsive and has a quick turnaround time (e.g., takes around 3 weeks to design the entire issue).

For this contest, please design a cover and article. Please refer to our last two issues (links above) before designing. We would like to see how the designer can take the images and edit them in a way that incorporates them seamlessly into the magazine as has been done in the past. Our end goal will be for the designer to design the entire issue and future issues. We anticipate this contest will not cover the entire cost of the work for completing the issue. When we find a designer we like, we will work out details for additional payment. Images can be found here: https://files.quorvanshare.net/folders/7KpTzRwq2LmXvNb4Hs9JdYeCa0FgUi3Q?usp=sharing

```html
<!DOCTYPE html>
<html lang="en">
<head>
<meta charset="utf-8">
<title>Dialysis, Caregiving &amp; Emotional Health</title>
<link rel="stylesheet" href="https://fonts.googleapis.com/css2?family=Archivo+Black&family=Noto+Serif:wght@400;700&family=PT+Serif:wght@400&display=swap">
<style>
  :root {
    --page-bg: #ece9e5;
    --title-green: #033a35;
    --accent-pink: #d89bbd;
    --body-ink: #2a2a2a;
    --photo-wall: #e9e6e2;
    --photo-green: #4f5a2e;
    --photo-teal: #234a44;
    --photo-pink: #c98aa6;
    --photo-sofa: #6c6661;
  }
  * { margin: 0; padding: 0; box-sizing: border-box; }
  html, body {
    width: 927px; height: 1200px; overflow: hidden;
    background: var(--page-bg);
  }
  .page {
    position: relative; width: 927px; height: 1200px; overflow: hidden;
    background: var(--page-bg);
  }
  .feature-photo {
    position: absolute; left: 0; top: 440px; width: 927px; height: 760px;
    background:
      radial-gradient(ellipse 260px 200px at 560px 560px, var(--photo-pink) 0%, rgba(201,138,166,0) 100%),
      radial-gradient(ellipse 380px 260px at 200px 660px, var(--photo-green) 0%, rgba(79,90,46,0) 100%),
      radial-gradient(ellipse 260px 300px at 220px 260px, var(--photo-teal) 0%, rgba(35,74,68,0) 100%),
      radial-gradient(ellipse 200px 260px at 860px 640px, var(--photo-sofa) 0%, rgba(108,102,97,0) 100%),
      linear-gradient(to bottom, var(--photo-wall) 0%, #ddd7d1 100%);
  }
  .headline {
    position: absolute; inset: 0;
    font-family: "Archivo Black", "Arial Black", sans-serif;
    color: var(--title-green);
    line-height: 1;
  }
  .headline span { position: absolute; white-space: nowrap; letter-spacing: -1px; }
  .headline .line-1 { left: 30px; top: 44px; font-size: 88px; }
  .headline .line-2 { left: 100px; top: 134px; font-size: 88px; }
  .headline .line-3 { right: 58px; top: 246px; font-size: 88px; }
  .headline .line-4 { right: 58px; top: 338px; font-size: 88px; }
  .ampersand {
    position: absolute; left: 120px; top: 210px;
    font-family: "PT Serif", "Times New Roman", serif;
    font-size: 300px; line-height: 1;
    color: var(--accent-pink);
  }
  .byline {
    position: absolute; right: 58px; top: 442px;
    font-family: "Noto Serif", Georgia, serif; font-weight: 700;
    font-size: 28px; color: var(--accent-pink);
  }
  .intro {
    position: absolute; right: 55px; width: 440px;
    font-family: "Noto Serif", Georgia, serif;
    font-size: 14.5px; line-height: 21.8px;
    color: var(--body-ink); text-align: right;
  }
  .intro-lead { top: 490px; }
  .intro-follow { top: 642px; }
</style>
</head>
<body>
<main class="page">
  <div class="feature-photo" role="img" aria-label="Photo of a smiling older man wrapping a knitted green blanket around the shoulders of a smiling older woman seated on a sofa"></div>

  <h1 class="headline">
    <span class="line-1">Dialysis,</span>
    <span class="line-2">Caregiving,</span>
    <span class="line-3">Emotional</span>
    <span class="line-4">Health</span>
  </h1>
  <div class="ampersand" aria-hidden="true">&amp;</div>
  <p class="byline">By Maren Ostlund</p>

  <p class="intro intro-lead">Dialysis is life-changing in many ways. It may be<br>what makes your life possible, for one. But it may<br>also significantly impact your daily routine, your<br>sense of self and your relationships—and it may<br>impact all three if your significant other or another<br>close relative has taken on a caregiving role.</p>

  <p class="intro intro-follow">You and your caregiver maybe new to<br>this situation or coping with<br>it long-term. Either way,<br>psychologists and<br>social workers who work with<br>people with kidney disease<br>and other chronic illnesses<br>can help<br>you both manage your<br>routines, navigate conflicts<br>and maintain—or even enrich—<br>your relationship through this<br>experience.</p>
</main>
</body>
</html>
```